Plumbing and heating business card design

i need a new business card for the company i work for called Dr. Brightpipe. It is a plumbing and heating company that has been operating for over 30 years. We are not like these big plumbing companies that have ways to charge the customer as much as possible. Our company does only what is necessary and what is needed to do the job right the first time without the high cost. we are a neighborhood business which kind of explains why we don't charge customers through the roof. I would like to see a design with a nice background anything but just plain white. maybe like a light blue at the top of the design. on the back of the card i would like it to say " T. Vandermeer's Dr. Brightpipe". maybe add some color to the lettering on the front of the card for example blue font for plumbing and red font for heating. raised print. im sure Cardolux designers will make it look good. The final design should help spread a good word about our company and help grow business.

Industry/Entity Type

Business

Contact Information for Business Card

Dr. Brightpipe, Plumbing & heating, Gordon Tasker, Northeast District Operations manager, 4827 Birchwell st., Office:(555)-284-1937, doctorbrightpipe@mailverra.net

Requirements
Must have
• raised print finish and a nice sturdy feel.

```html
<!DOCTYPE html>
<html lang="en">
<head>
<meta charset="UTF-8">
<title>Dr. Brightpipe — Business Card</title>
<link href="https://fonts.googleapis.com/css2?family=Montserrat:wght@400;500;700;800&display=swap" rel="stylesheet">
<style>
  :root {
    --stage: #e9eaec;
    --card-white: #ffffff;
    --charcoal: #2a2627;
    --charcoal-light: #3a3536;
    --brand-blue: #1d6fc0;
    --brand-red: #e03a2b;
    --accent-orange: #f06a2a;
    --text-light: #f2f2f2;
    --text-muted: #bdbdbd;
    --tagline: #6c6c6c;
  }
  * { box-sizing: border-box; margin: 0; padding: 0; }
  html, body { width: 1200px; height: 876px; overflow: hidden; }
  body {
    background: var(--stage);
    font-family: "Montserrat", Arial, sans-serif;
    display: flex;
    align-items: center;
    justify-content: center;
    gap: 60px;
  }
  .card {
    position: relative;
    width: 525px;
    height: 300px;
    border-radius: 4px;
    overflow: hidden;
    background: var(--card-white);
    box-shadow: 0 10px 30px rgba(0,0,0,0.18);
  }

  /* Back: contact side */
  .card-back .contact-panel {
    position: absolute;
    inset: 0 0 auto 0;
    height: 170px;
    background: linear-gradient(135deg, var(--charcoal-light), var(--charcoal));
    clip-path: polygon(0 0, 100% 0, 100% 82%, 0 100%);
    padding: 24px 30px;
  }
  .holder { text-align: right; color: var(--text-light); }
  .holder-name { font-size: 24px; font-weight: 700; letter-spacing: 0.3px; }
  .holder-title { font-size: 10px; font-weight: 400; color: var(--text-muted); margin-top: 2px; }
  .contact-list { list-style: none; margin-top: 10px; }
  .contact-item {
    display: flex; align-items: center; gap: 14px;
    color: var(--text-light); font-size: 12px; font-weight: 500;
    height: 28px;
  }
  .contact-icon {
    width: 22px; height: 22px; border-radius: 3px;
    background: var(--brand-blue);
    display: flex; align-items: center; justify-content: center;
  }
  .card-back .red-edge {
    position: absolute; left: 0; bottom: 0;
    width: 12px; height: 148px;
    background: linear-gradient(to bottom, var(--brand-red), var(--accent-orange));
  }
  .card-back .brand-lockup {
    position: absolute; right: 40px; bottom: 26px;
  }

  /* Front: logo side */
  .card-front .side-band {
    position: absolute; left: 0; top: 0; bottom: 0; width: 18px;
    background: var(--charcoal);
  }
  .card-front .corner-blue {
    position: absolute; right: 0; top: 0; width: 90px; height: 18px;
    background: var(--brand-blue);
    clip-path: polygon(0 0, 100% 0, 100% 100%, 20% 100%);
  }
  .card-front .corner-red {
    position: absolute; left: 0; bottom: 0; width: 18px; height: 80px;
    background: linear-gradient(to bottom, var(--brand-red), var(--accent-orange));
  }
  .card-front .brand-lockup {
    position: absolute; left: 50%; top: 50%;
    transform: translate(-50%, -50%);
  }

  .brand-lockup { display: flex; align-items: center; gap: 14px; }
  .brand-dot {
    width: 44px; height: 44px; border-radius: 50%;
    background: var(--brand-blue); flex-shrink: 0;
  }
  .brand-text { line-height: 1.05; }
  .brand-name {
    font-size: 22px; font-weight: 800; color: var(--brand-blue);
    text-transform: uppercase; letter-spacing: 0.2px;
  }
  .brand-name .line { display: block; }
  .brand-tagline {
    font-size: 12px; font-weight: 400; color: var(--tagline);
    letter-spacing: 1.5px; margin-top: 4px;
  }
  .card-back .brand-name { font-size: 18px; }
  .card-back .brand-dot { width: 36px; height: 36px; }
  .card-back .brand-tagline { font-size: 10px; }
</style>
</head>
<body>

  <section class="card card-back" aria-label="Card back with contact details">
    <div class="contact-panel">
      <div class="holder">
        <p class="holder-name">Gordon Tasker</p>
        <p class="holder-title">Northeast District Operations manager</p>
      </div>
      <ul class="contact-list">
        <li class="contact-item">
          <span class="contact-icon">
            <svg width="12" height="12" viewBox="0 0 24 24" fill="#fff"><path d="M6.6 10.8a15.1 15.1 0 0 0 6.6 6.6l2.2-2.2a1 1 0 0 1 1-.25 11.4 11.4 0 0 0 3.6.57 1 1 0 0 1 1 1V20a1 1 0 0 1-1 1A17 17 0 0 1 3 4a1 1 0 0 1 1-1h3.5a1 1 0 0 1 1 1c0 1.25.2 2.45.57 3.57a1 1 0 0 1-.25 1z"/></svg>
          </span>
          (555)-284-1937
        </li>
        <li class="contact-item">
          <span class="contact-icon">
            <svg width="12" height="12" viewBox="0 0 24 24" fill="#fff"><path d="M12 3 2 12h3v8h5v-5h4v5h5v-8h3z"/></svg>
          </span>
          4827 Birchwell st.
        </li>
        <li class="contact-item">
          <span class="contact-icon">
            <svg width="12" height="12" viewBox="0 0 24 24" fill="none" stroke="#fff" stroke-width="2"><rect x="3" y="5" width="18" height="14" rx="1"/><path d="m3 6 9 7 9-7"/></svg>
          </span>
          doctorbrightpipe@mailverra.net
        </li>
      </ul>
    </div>
    <div class="red-edge"></div>
    <div class="brand-lockup">
      <span class="brand-dot"></span>
      <div class="brand-text">
        <p class="brand-name"><span class="line">T. Vandermeer's</span><span class="line">Dr. Brightpipe</span></p>
        <p class="brand-tagline">plumbing and heating</p>
      </div>
    </div>
  </section>

  <section class="card card-front" aria-label="Card front with company name">
    <div class="side-band"></div>
    <div class="corner-blue"></div>
    <div class="corner-red"></div>
    <div class="brand-lockup">
      <span class="brand-dot"></span>
      <div class="brand-text">
        <p class="brand-name"><span class="line">T. Vandermeer's</span><span class="line">Dr. Brightpipe</span></p>
        <p class="brand-tagline">plumbing and heating</p>
      </div>
    </div>
  </section>

</body>
</html>
```